Filter Cleaning Business requires an advertisement that can be used on billboards, trucks, magazines

I require an advertisement that can be used wherever required promoting the services of the business in short form attracting the attention of prospective customers and making them want more information.
We also need to promote the companies philosophy to assist business improve and form partnerships in achieving this. Also that the company has proven with existing customers the ability to achieve this.
The company already has a logo and want the ad to align with the logo.

Target Market(s)

The target market is mainly Mining, Construction, Energy and Heavy Industrial companies.

Industry/Entity Type

Business

Requirements
Must have
• The ad must include the company logo
Nice to have
• The ad would include pictures of different kinds of filters serviced by the company.

```html
<!DOCTYPE html>
<html lang="en">
<head>
<meta charset="utf-8">
<title>Southland Filter Cleaning Services – Advertisement</title>
<link href="https://fonts.googleapis.com/css2?family=Arimo:wght@400;700&family=Roboto+Condensed:wght@700&display=swap" rel="stylesheet">
<style>
  :root {
    --backdrop: #231f20;
    --green: #0b9446;
    --green-light: #5cb947;
    --ink: #1c1c1c;
    --white: #ffffff;
    --filter-grey: #9a9a95;
    --filter-dark: #5d5d58;
  }
  html, body {
    margin: 0;
    width: 1200px;
    height: 1000px;
    overflow: hidden;
    background: var(--backdrop);
    font-family: "Arimo", Arial, sans-serif;
  }
  .flyer {
    position: absolute;
    left: 231px;
    top: 22px;
    width: 739px;
    height: 956px;
    background: linear-gradient(to bottom,
      var(--white) 0px, var(--white) 150px,
      #d9eedf 230px, #5fb97b 330px,
      var(--green) 430px, var(--green) 956px);
    overflow: hidden;
  }
  .brand {
    position: absolute;
    top: 18px;
    left: 0;
    width: 100%;
    text-align: center;
  }
  .brand-dot {
    width: 56px;
    height: 56px;
    border-radius: 50%;
    background: var(--green-light);
    margin: 0 auto 14px;
  }
  .brand-name {
    font-size: 16px;
    font-weight: 400;
    color: var(--green-light);
    letter-spacing: 2px;
    line-height: 19px;
    text-transform: uppercase;
  }
  .benefits, .features {
    position: absolute;
    left: 0;
    width: 100%;
    text-align: center;
    font-weight: 700;
    font-size: 17px;
    line-height: 22px;
  }
  .benefits { top: 162px; color: var(--ink); }
  .features { top: 600px; color: var(--white); }
  .features .features-title {
    color: var(--ink);
    font-size: 19px;
    line-height: 23px;
  }
  .item::before {
    content: "";
    display: inline-block;
    width: 6px;
    height: 6px;
    background: currentColor;
    margin: 0 4px 3px 4px;
  }
  .features .item::before { background: var(--ink); }
  .product-photo {
    position: absolute;
    left: 140px;
    top: 268px;
    width: 460px;
    height: 320px;
  }
  .offer-box {
    position: absolute;
    left: 32px;
    top: 745px;
    width: 680px;
    height: 124px;
    border: 1px dashed rgba(255,255,255,0.8);
    border-radius: 14px;
    text-align: center;
  }
  .offer-headline {
    font-family: "Roboto Condensed", "Arial Narrow", sans-serif;
    font-weight: 700;
    font-size: 25px;
    line-height: 29px;
    color: var(--ink);
    margin-top: 10px;
  }
  .offer-copy {
    font-size: 11.5px;
    font-weight: 700;
    color: var(--white);
    line-height: 15px;
    margin: 10px 30px 0;
  }
  .contact-cta {
    position: absolute;
    left: 176px;
    top: 900px;
    font-family: "Roboto Condensed", "Arial Narrow", sans-serif;
    font-weight: 700;
    font-size: 22px;
    color: var(--white);
  }
  .contact-details {
    position: absolute;
    left: 389px;
    top: 886px;
    font-size: 17px;
    font-weight: 700;
    line-height: 24px;
    color: var(--white);
  }
</style>
</head>
<body>
  <main class="flyer">
    <header class="brand">
      <div class="brand-dot"></div>
      <div class="brand-name">Southland<br>Filter Cleaning Services</div>
    </header>

    <section class="benefits">
      <div><span class="item">Recycle</span><span class="item">Re-use</span><span class="item">Reduce landfill impact</span></div>
      <div><span class="item">Save you 40 – 60 % off new filter by recycling your filters</span></div>
      <div><span class="item">Reduces operating expenses</span><span class="item">Increase carbon credits</span></div>
      <div><span class="item">Reduce Inventory</span></div>
    </section>

    <svg class="product-photo" viewBox="0 0 460 320" role="img" aria-label="Photo of assorted cylindrical industrial air filters grouped together">
      <defs>
        <linearGradient id="filterTone" x1="0" y1="0" x2="1" y2="1">
          <stop offset="0" stop-color="#c9c9c3"/>
          <stop offset="0.6" stop-color="#9a9a95"/>
          <stop offset="1" stop-color="#5d5d58"/>
        </linearGradient>
      </defs>
      <rect width="460" height="320" rx="6" fill="url(#filterTone)" opacity="0.85"/>
    </svg>

    <section class="features">
      <div class="features-title">Southland Filter Cleaning Services</div>
      <div><span class="item">Uses no water or chemicals</span> <span class="item">Uses clean air to blow and vacuum</span></div>
      <div><span class="item">Inspects every filter for integrity</span> <span class="item">Track filter cleaning cycles</span></div>
      <div><span class="item">Vacuum tests every filter</span> <span class="item">Heavyline compliant process</span></div>
      <div><span class="item">Provides filter test reports</span></div>
    </section>

    <section class="offer-box">
      <div class="offer-headline">“We can come to you” to clean your filters!<br>You get “your” filter returned!</div>
      <p class="offer-copy">We’re confident in our company and in our product. We are sure that you will be, too. Contact us today to start saving the environment and start saving money by using recycled filters.</p>
    </section>

    <div class="contact-cta">Contact us today</div>
    <div class="contact-details">
      <div>Phone;&nbsp; 0400 123 456</div>
      <div>Email; info@southlandfilters.com.au</div>
    </div>
  </main>
</body>
</html>
```